Business Card Design

About Us
VaultNet is a young and innovative company focusing on security and hosting solutions for global enterprise. To supply the high-performance, highly interconnected and low latency DDoS protection service, we distributed a large number of huge scrubbing centers all over the world. So VaultNet is the first choice for enterprise to protect their network security.

Task detail
1. We hope that the business card can be filled with creativity, simple and technologe, the business card background is white, the business card text color and other colors are black, blue, green or your needs.

2. We need the source files provided by the successful bidder, such as *.psd, *.ai, etc.

3. One side contains the following:
-Logo
-Marco Sales Manager
-VAULTNET TECHNOLOGY CO., LIMITED
-Add:
9/F., Harbourgate Tower,
318 Pelton Avenue, Tsimwell, Kowloon,
HK
-Tel: 86-755-4719 2058
-Phone: 86-189 6140 3527
-Email: marco@vault-netz.example
-Web: www.vault-netz.example

4. The other side contains the following:
-Logo

5. Please find the attachment contains the logo PSD source files.

```html
<!DOCTYPE html>
<html lang="en">
<head>
<meta charset="utf-8">
<title>VaultNet Business Card</title>
<link rel="stylesheet" href="https://fonts.googleapis.com/css2?family=Lato:wght@400;700;900&display=swap">
<style>
  :root {
    --backdrop: #2a2a2a;
    --card: #f7f7f7;
    --ink: #2b2b2b;
    --ink-soft: #4a4a4a;
    --teal: #2fa3b5;
    --green: #6cbf2a;
  }
  * { margin: 0; padding: 0; box-sizing: border-box; }
  html, body { width: 1200px; height: 997px; overflow: hidden; }
  body {
    background: var(--backdrop);
    font-family: 'Lato', Arial, sans-serif;
    color: var(--ink);
    position: relative;
  }
  .card {
    position: absolute;
    width: 560px;
    height: 320px;
    background: var(--card);
    border-radius: 22px;
    box-shadow: 0 18px 40px rgba(0,0,0,.55);
  }
  .card--front { left: 70px; top: 110px; }
  .card--back  { left: 570px; top: 520px; }

  .brand { display: flex; align-items: center; gap: 12px; }
  .brand__square { width: 34px; height: 34px; background: var(--teal); }
  .brand__name { font-weight: 900; color: var(--green); letter-spacing: .5px; }

  .card--front .brand {
    position: absolute; left: 50%; top: 50%;
    transform: translate(-50%, -50%);
  }
  .card--front .brand__square { width: 58px; height: 58px; }
  .card--front .brand__name { font-size: 62px; line-height: 1; }

  .card--back .brand { position: absolute; left: 32px; top: 34px; }
  .card--back .brand__name { font-size: 34px; line-height: 1; }

  .person { position: absolute; right: 34px; top: 38px; text-align: right; }
  .person__name { font-weight: 700; font-size: 18px; color: var(--green); }
  .person__role { font-size: 11px; letter-spacing: .8px; margin-top: 2px; }

  .rule {
    position: absolute; height: 4px;
    background: repeating-linear-gradient(90deg, var(--teal) 0 22px, #fff 22px 24px);
  }
  .rule--top { right: 34px; top: 92px; width: 170px; }
  .rule--mid { left: 32px; right: 34px; top: 165px; }

  .company {
    position: absolute; right: 34px; top: 102px;
    font-size: 12.5px; letter-spacing: .4px;
  }
  .company strong { font-weight: 700; }

  .web {
    position: absolute; left: 32px; top: 144px;
    font-weight: 700; font-size: 12px;
  }

  .contacts { position: absolute; left: 32px; top: 186px; list-style: none; }
  .contacts li {
    display: flex; align-items: center; gap: 12px;
    font-size: 12.5px; margin-bottom: 12px;
  }
  .contacts svg { width: 16px; height: 16px; fill: none; stroke: var(--green); stroke-width: 1.8; }

  .address {
    position: absolute; right: 34px; top: 186px; text-align: right;
    font-weight: 700; font-size: 11.5px; line-height: 1.6; color: var(--green);
    font-style: normal;
  }
</style>
</head>
<body>

  <section class="card card--front" aria-label="Card front">
    <div class="brand">
      <span class="brand__square"></span>
      <span class="brand__name">VaultNet</span>
    </div>
  </section>

  <section class="card card--back" aria-label="Card back">
    <div class="brand">
      <span class="brand__square"></span>
      <span class="brand__name">VaultNet</span>
    </div>

    <div class="person">
      <p class="person__name">Marco</p>
      <p class="person__role">SALES MANAGER</p>
    </div>
    <div class="rule rule--top"></div>
    <p class="company">VAULTNET <strong>TECHNOLOGY CO., LIMITED</strong></p>

    <p class="web">www.vault-netz.example</p>
    <div class="rule rule--mid"></div>

    <ul class="contacts">
      <li>
        <svg viewBox="0 0 16 16" aria-hidden="true"><rect x="4" y="1.5" width="8" height="13" rx="1.5"/><line x1="7" y1="12" x2="9" y2="12"/></svg>
        86-755-4719 2058
      </li>
      <li>
        <svg viewBox="0 0 16 16" aria-hidden="true"><path d="M2 6c0-2 2-3 6-3s6 1 6 3l-3 1-1-2H6L5 7 2 6z"/><rect x="3" y="8" width="10" height="6" rx="1"/></svg>
        86-189 6140 3527
      </li>
      <li>
        <svg viewBox="0 0 16 16" aria-hidden="true"><rect x="1.5" y="3.5" width="13" height="9"/><polyline points="1.5,3.5 8,9 14.5,3.5"/></svg>
        marco@vault-netz.example
      </li>
    </ul>

    <address class="address">
      9/F., Harbourgate Tower<br>
      318 Pelton Avenue, Tsimwell, Kowloon, HK
    </address>
  </section>

</body>
</html>
```